5 Blog Posts and Lead Magnet Needs Branding for Remodeling Company

I have 5 blogs and a website lead magnet that have content written but need some design and layout help to align with my brand identity. The content will need to be formatted for social media and website. I have a logo, colors and font. I also have a website I'm pretty happy with right now that can provide direction.
Target Market(s)
Age 40-65, Average salary 250K, Male/Female Professional College + Married 3 + Mid-full size car with high end finishes.
Industry/Entity Type
Construction, remodeling
Colors
Designer to choose colors to be used in the design.
Look and feel

```html
<!DOCTYPE html>
<html lang="en">
<head>
<meta charset="utf-8">
<title>Larkwell Home Improvements — Blog Page Templates</title>
<link rel="stylesheet" href="https://fonts.googleapis.com/css2?family=Montserrat:wght@300;400;500;600;800&display=swap">
<style>
  :root {
    --navy: #0c1a4a;
    --green: #8dc63f;
    --backdrop: #e6e6e6;
    --paper: #ffffff;
    --subtle: #8a8fa3;
    --body-ink: #3b4573;
    --image-tint: #5d6689;
  }
  * { margin: 0; padding: 0; box-sizing: border-box; }
  html, body { width: 960px; height: 1200px; overflow: hidden; background: var(--backdrop); }
  body { position: relative; font-family: "Montserrat", sans-serif; color: var(--navy); }

  .page { position: absolute; width: 432px; height: 540px; background: var(--paper); overflow: hidden; }
  .page--cover { left: 24px; top: 30px; background: var(--navy); }
  .page--two-column { left: 504px; top: 30px; }
  .page--feature { left: 24px; top: 630px; }
  .page--feature-dark { left: 504px; top: 630px; }

  .corner { position: absolute; right: 0; top: 0; width: 48px; height: 48px; }

  .cover-topic { position: absolute; left: 0; right: 0; top: 240px; text-align: center;
    font-weight: 800; font-size: 52px; letter-spacing: 0.5px; color: var(--paper); }

  .page-title { position: absolute; left: 34px; top: 28px; font-weight: 800; font-size: 22px; line-height: 1; }
  .page-subtitle { position: absolute; left: 34px; top: 56px; font-weight: 300; font-size: 17px; color: var(--subtle); line-height: 1; }

  .section { position: absolute; overflow: hidden; }
  .section h2 { font-weight: 500; font-size: 12.5px; line-height: 1; margin-bottom: 6px; }
  .section p { font-size: 7.1px; line-height: 9px; color: var(--body-ink); }
  .section p.lead { text-indent: 14px; }

  .image-slot { position: absolute; background: var(--navy); }

  .dark-band { position: absolute; left: 0; top: 94px; width: 432px; height: 446px; background: var(--navy); }
  .page--feature-dark .section h2 { color: var(--green); }
  .page--feature-dark .section p { color: var(--paper); }
  .page--feature-dark .image-slot { background: var(--image-tint); }

  .rule { position: absolute; height: 1.5px; background: var(--navy); }
  .page--cover .rule, .page--feature-dark .rule { background: var(--paper); }

  .brand { position: absolute; text-align: center; line-height: 1; color: var(--navy); }
  .brand-name { display: block; font-weight: 600; font-size: 15px; }
  .brand-tag { display: block; font-weight: 600; font-size: 3.6px; letter-spacing: 0.6px; margin-top: 3px; }
  .page--cover .brand, .page--feature-dark .brand { color: var(--paper); }
</style>
</head>
<body>

<!-- Cover -->
<section class="page page--cover">
  <h1 class="cover-topic">TOPIC</h1>
  <div class="rule" style="left:37px; top:499px; width:139px;"></div>
  <div class="rule" style="left:256px; top:499px; width:140px;"></div>
  <div class="brand" style="left:176px; top:488px; width:80px;">
    <span class="brand-name">Larkwell</span>
    <span class="brand-tag">— HOME IMPROVEMENTS —</span>
  </div>
</section>

<!-- Two-column article -->
<section class="page page--two-column">
  <svg class="corner" viewBox="0 0 48 48" aria-hidden="true"><polygon points="0,0 48,0 48,48" fill="#0c1a4a"/></svg>
  <h1 class="page-title">TITLE</h1>
  <p class="page-subtitle">Sub Title</p>

  <article class="section" style="left:32px; top:103px; width:178px; height:250px;">
    <h2>TITLE #1</h2>
    <p class="lead">Lorem ipsum dolor sit amet, consectetuer adipiscing elit, sed diam nonummy nibh euismod tincidunt ut laoreet dolore magna aliquam erat volutpat. Ut wisi enim ad minim veniam, quis nostrud exerci tation ullamcorper suscipit lobortis nisl ut aliquip ex ea commodo consequat. Duis autem vel eum iriure dolor in hendrerit in vulputate velit esse molestie consequat, vel illum dolore eu feugiat nulla facilisis at vero eros et accumsan et iusto odio dignissim qui blandit praesent luptatum zzril delenit augue duis dolore te feugait nulla facilisi.</p>
    <p>Lorem ipsum dolor sit amet, cons ectetuer adipiscing elit, sed diam nonummy nibh euismod tincidunt ut laoreet dolore magna aliquam erat volutpat. Ut wisi enim ad minim veniam, quis nostrud exerci tation ullamcorper suscipit lobortis nisl ut aliquip ex ea commodo Lorem ipsum dolor sit amet, consectetuer adipiscing elit, sed diam nonummy nibh euismod tincidunt ut laoreet dolore magna aliquam erat volutpat. Ut wisi enim ad minim veniam, quis nostrud exerci tation ullamcorper suscipit lobortis nisl ut aliquip ex ea commodo</p>
  </article>

  <article class="section" style="left:32px; top:361px; width:178px; height:130px;">
    <h2>TITLE #2</h2>
    <p class="lead">Lorem ipsum dolor sit amet, consectetuer adipiscing elit, sed diam nonummy nibh euismod tincidunt ut laoreet dolore magna aliquam erat volutpat. Ut wisi enim ad minim veniam, quis nostrud exerci tation ullamcorper suscipit lobortis nisl ut aliquip ex ea commodo consequat. Duis autem vel eum iriure dolor in hendrerit in vulputate velit esse molestie consequat, vel illum dolore eu feugiat nulla facilisis at vero eros et accumsan et iusto odio dignissim qui blandit praesent luptatum zzril delenit augue duis dolore te feugait nulla</p>
  </article>

  <article class="section" style="left:222px; top:103px; width:178px; height:128px;">
    <h2>TITLE #3</h2>
    <p class="lead">Lorem ipsum dolor sit amet, consectetuer adipiscing elit, sed diam nonummy nibh euismod tincidunt ut laoreet dolore magna aliquam erat volutpat. Ut wisi enim ad minim veniam, quis nostrud exerci tation ullamcorper suscipit lobortis nisl ut aliquip ex ea commodo consequat. Duis autem vel eum iriure dolor in hendrerit in vulputate velit esse molestie consequat, vel illum dolore eu feugiat nulla facilisis at vero eros et accumsan et iusto odio dignissim qui blandit praesent luptatum zzril delenit augue duis dolore te feugait nulla</p>
  </article>

  <article class="section" style="left:222px; top:244px; width:178px; height:248px;">
    <h2>TITLE #4</h2>
    <p class="lead">Lorem ipsum dolor sit amet, consectetuer adipiscing elit, sed diam nonummy nibh euismod tincidunt ut laoreet dolore magna aliquam erat volutpat. Ut wisi enim ad minim veniam, quis nostrud exerci tation ullamcorper suscipit lobortis nisl ut aliquip ex ea commodo consequat. Duis autem vel eum iriure dolor in hendrerit in vulputate velit esse molestie consequat, vel illum dolore eu feugiat nulla facilisis at vero eros et accumsan et iusto odio dignissim qui blandit praesent luptatum zzril delenit augue duis dolore te feugait nulla facilisi.</p>
    <p>Lorem ipsum dolor sit amet, cons ectetuer adipiscing elit, sed diam nonummy nibh euismod tincidunt ut laoreet dolore magna aliquam erat volutpat. Ut wisi enim ad minim veniam, quis nostrud exerci tation ullamcorper suscipit lobortis nisl ut aliquip ex ea commodo Lorem ipsum dolor sit amet, consectetuer adipiscing elit, sed diam nonummy nibh euismod tincidunt ut laoreet dolore magna aliquam erat volutpat. Ut wisi enim ad minim veniam, quis nostrud exerci tation ullamcorper suscipit lobortis nisl ut aliquip ex ea commodo</p>
  </article>

  <div class="rule" style="left:36px; top:515px; width:278px;"></div>
  <div class="brand" style="left:322px; top:504px; width:80px;">
    <span class="brand-name">Larkwell</span>
    <span class="brand-tag">— HOME IMPROVEMENTS —</span>
  </div>
</section>

<!-- Feature article, light -->
<section class="page page--feature">
  <svg class="corner" viewBox="0 0 48 48" aria-hidden="true"><polygon points="0,0 48,0 48,48" fill="#0c1a4a"/></svg>
  <h1 class="page-title">TITLE</h1>
  <p class="page-subtitle">Sub Title</p>

  <article class="section" style="left:32px; top:103px; width:368px; height:130px;">
    <h2>TITLE #1</h2>
    <p class="lead">Lorem ipsum dolor sit amet, consectetuer adipiscing elit, sed diam nonummy nibh euismod tincidunt ut laoreet dolore magna aliquam erat volutpat. Ut wisi enim ad minim veniam, quis nostrud exerci tation ullamcorper suscipit lobortis nisl ut aliquip ex ea commodo consequat. Duis autem vel eum iriure dolor in hendrerit in vulputate velit esse molestie consequat, vel illum dolore eu feugiat nulla facilisis at vero eros et accumsan et iusto odio dignissim qui blandit praesent luptatum zzril delenit augue duis dolore te feugait nulla facilisi.</p>
    <p>Lorem ipsum dolor sit amet, cons ectetuer adipiscing elit, sed diam nonummy nibh euismod tincidunt ut laoreet dolore magna aliquam erat volutpat. Ut wisi enim ad minim veniam, quis nostrud exerci tation ullamcorper suscipit lobortis nisl ut aliquip ex ea commodo Lorem ipsum dolor sit amet, consectetuer adipiscing elit, sed diam nonummy nibh euismod tincidunt ut laoreet dolore magna aliquam erat volutpat. Ut wisi enim ad minim veniam, quis nostrud exerci tation ullamcorper suscipit lobortis nisl ut aliquip ex ea commodo</p>
  </article>

  <div class="image-slot" role="img" aria-label="Photo of a finished home remodel" style="left:32px; top:245px; width:178px; height:245px;"></div>

  <article class="section" style="left:222px; top:244px; width:178px; height:125px;">
    <h2>TITLE #2</h2>
    <p class="lead">Lorem ipsum dolor sit amet, consectetuer adipiscing elit, sed diam nonummy nibh euismod tincidunt ut laoreet dolore magna aliquam erat volutpat. Ut wisi enim ad minim veniam, quis nostrud exerci tation ullamcorper suscipit lobortis nisl ut aliquip ex ea commodo consequat. Duis autem vel eum iriure dolor in hendrerit in vulputate velit esse molestie consequat, vel illum dolore eu feugiat nulla facilisis at vero eros et accumsan et iusto odio dignissim qui blandit praesent luptatum zzril</p>
  </article>

  <article class="section" style="left:222px; top:375px; width:178px; height:125px;">
    <h2>TITLE #3</h2>
    <p class="lead">Lorem ipsum dolor sit amet, consectetuer adipiscing elit, sed diam nonummy nibh euismod tincidunt ut laoreet dolore magna aliquam erat volutpat. Ut wisi enim ad minim veniam, quis nostrud exerci tation ullamcorper suscipit lobortis nisl ut aliquip ex ea commodo consequat. Duis autem vel eum iriure dolor in hendrerit in vulputate velit esse molestie consequat, vel illum dolore eu feugiat nulla facilisis at vero eros et accumsan et iusto odio dignissim qui blandit praesent luptatum zzril</p>
  </article>

  <div class="rule" style="left:36px; top:514px; width:278px;"></div>
  <div class="brand" style="left:322px; top:503px; width:80px;">
    <span class="brand-name">Larkwell</span>
    <span class="brand-tag">— HOME IMPROVEMENTS —</span>
  </div>
</section>

<!-- Feature article, dark -->
<section class="page page--feature-dark">
  <div class="dark-band"></div>
  <svg class="corner" viewBox="0 0 48 48" aria-hidden="true"><polygon points="0,0 48,0 48,48" fill="#0c1a4a"/></svg>
  <h1 class="page-title">TITLE</h1>
  <p class="page-subtitle">Sub Title</p>

  <article class="section" style="left:32px; top:102px; width:368px; height:130px;">
    <h2>TITLE #1</h2>
    <p class="lead">Lorem ipsum dolor sit amet, consectetuer adipiscing elit, sed diam nonummy nibh euismod tincidunt ut laoreet dolore magna aliquam erat volutpat. Ut wisi enim ad minim veniam, quis nostrud exerci tation ullamcorper suscipit lobortis nisl ut aliquip ex ea commodo consequat. Duis autem vel eum iriure dolor in hendrerit in vulputate velit esse molestie consequat, vel illum dolore eu feugiat nulla facilisis at vero eros et accumsan et iusto odio dignissim qui blandit praesent luptatum zzril delenit augue duis dolore te feugait nulla facilisi.</p>
    <p>Lorem ipsum dolor sit amet, cons ectetuer adipiscing elit, sed diam nonummy nibh euismod tincidunt ut laoreet dolore magna aliquam erat volutpat. Ut wisi enim ad minim veniam, quis nostrud exerci tation ullamcorper suscipit lobortis nisl ut aliquip ex ea commodo Lorem ipsum dolor sit amet, consectetuer adipiscing elit, sed diam nonummy nibh euismod tincidunt ut laoreet dolore magna aliquam erat volutpat. Ut wisi enim ad minim veniam, quis nostrud exerci tation ullamcorper suscipit lobortis nisl ut aliquip ex ea commodo</p>
  </article>

  <div class="image-slot" role="img" aria-label="Photo of a finished home remodel" style="left:32px; top:244px; width:178px; height:246px;"></div>

  <article class="section" style="left:222px; top:243px; width:178px; height:125px;">
    <h2>TITLE #2</h2>
    <p class="lead">Lorem ipsum dolor sit amet, consectetuer adipiscing elit, sed diam nonummy nibh euismod tincidunt ut laoreet dolore magna aliquam erat volutpat. Ut wisi enim ad minim veniam, quis nostrud exerci tation ullamcorper suscipit lobortis nisl ut aliquip ex ea commodo consequat. Duis autem vel eum iriure dolor in hendrerit in vulputate velit esse molestie consequat, vel illum dolore eu feugiat nulla facilisis at vero eros et accumsan et iusto odio dignissim qui blandit praesent luptatum zzril</p>
  </article>

  <article class="section" style="left:222px; top:374px; width:178px; height:125px;">
    <h2>TITLE #3</h2>
    <p class="lead">Lorem ipsum dolor sit amet, consectetuer adipiscing elit, sed diam nonummy nibh euismod tincidunt ut laoreet dolore magna aliquam erat volutpat. Ut wisi enim ad minim veniam, quis nostrud exerci tation ullamcorper suscipit lobortis nisl ut aliquip ex ea commodo consequat. Duis autem vel eum iriure dolor in hendrerit in vulputate velit esse molestie consequat, vel illum dolore eu feugiat nulla facilisis at vero eros et accumsan et iusto odio dignissim qui blandit praesent luptatum zzril</p>
  </article>

  <div class="rule" style="left:36px; top:514px; width:278px;"></div>
  <div class="brand" style="left:322px; top:503px; width:80px;">
    <span class="brand-name">Larkwell</span>
    <span class="brand-tag">— HOME IMPROVEMENTS —</span>
  </div>
</section>

</body>
</html>
```